Re jig a A4 Instructional Flyer

We need an established A4 instructional Flyer (2 pages x A4) - to be rejigged in Harlow Academy of Learning Branding to look fresh and new.

Permissions have been received to rejig this Medical Triage Chart. Fresh branding and setting out (fonts) required.

FOOTER NOTES : to be inserted at the bottom of the A4 instruction sheet

Harlow Academy produced with permissions from Coastal Care Alliance, produced by Coastal Care Alliance with Clinic Circle Eastgate with permissions from Southern Basin Careline Hub. Harlow acknowledges the FMPCB Standards Criterion 3.2.3 Practice Training and Education in Triage

Target Market(s)

Medical Practices

Industry/Entity Type

Health

Font styles to use
Serif

Colors
0255a3
f78f20

Requirements
Must have
• Professional
• Pops of colour in the chart.
• This chart is to be USED and is VISUAL (no boring grey words throughout)
• PROBS SANS SERIF but SERIF for titles OK
Nice to have
• look at www.harlowlearning.edu.au FOR BRANDING look and feel

```html
<!DOCTYPE html>
<html lang="en">
<head>
<meta charset="utf-8">
<title>Triage Guide – Harlow Academy of Learning</title>
<link rel="stylesheet" href="https://fonts.googleapis.com/css2?family=Montserrat:wght@600;700;800&family=Open+Sans:ital,wght@0,400;0,600;0,700;1,400&display=swap">
<style>
:root{
  --navy:#0b3d8c;
  --navy-deep:#082c6a;
  --blue:#0255a3;
  --blue-light:#1f74c9;
  --orange:#f78f20;
  --grey-pill:#c9ccd1;
  --grey-dark:#5c6066;
  --ink:#2b2f36;
  --muted:#5d636b;
  --panel:#eef1f5;
  --stage:#505256;
}
*{margin:0;padding:0;box-sizing:border-box}
html,body{width:888px;height:1200px;overflow:hidden;background:var(--stage)}
body{position:relative;font-family:"Open Sans",Arial,sans-serif;color:var(--ink)}
.page{position:absolute;left:38px;width:765px;background:#fff;overflow:hidden}
.sheet-front{top:30px;height:540px}
.sheet-back{top:616px;height:535px}
.abs{position:absolute}

/* ticks */
.ticks{list-style:none}
.ticks li{position:relative;padding-left:12px}
.ticks li::before{content:"";position:absolute;left:0;top:.25em;width:7px;height:7px;border:1px solid var(--orange);border-radius:1px}
.ticks li::after{content:"";position:absolute;left:2.6px;top:calc(.25em - 1px);width:2.6px;height:5.5px;border:solid var(--orange);border-width:0 1.3px 1.3px 0;transform:rotate(40deg)}
.ticks.navy li::before{border-color:var(--blue)}
.ticks.navy li::after{border-color:var(--blue)}

/* ---------- FRONT ---------- */
.front-header{left:0;top:0}
.brand{left:20px;top:26px;width:124px;text-align:center;color:var(--navy);font-weight:700;font-size:11px;line-height:1.25;letter-spacing:.5px}
.brand-mark{display:block;width:18px;height:18px;margin:0 auto 6px;background:var(--navy)}
.doc-title{left:214px;top:22px;width:398px;text-align:center;color:#fff;font-family:"Montserrat",sans-serif;font-weight:800;font-size:14px;line-height:23px;letter-spacing:-.1px;white-space:nowrap}
.tool-badge{left:620px;top:36px;width:145px;height:32px;background:var(--orange);color:#fff;display:flex;align-items:center;justify-content:center;gap:6px;font-family:"Montserrat",sans-serif;font-weight:800;font-size:24px;letter-spacing:.5px}

.pill{position:absolute;display:flex;align-items:center;justify-content:center;text-align:center;color:#fff;font-family:"Montserrat",sans-serif;font-weight:700;font-size:10px;line-height:1.25;border-radius:3px}
.pill-orange{background:var(--orange)}
.pill-navy{background:var(--navy)}
.pill-grey{background:var(--grey-pill);font-size:11px}
.pill-two{font-size:8.8px;line-height:1.3;white-space:nowrap}

.infobox{position:absolute;border:1px dashed #b9bec6;font-size:7.8px;line-height:1.5}
.infobox-head{color:#fff;font-family:"Montserrat",sans-serif;font-weight:700;font-size:10.5px;text-align:center;padding:3px 0}
.infobox .ticks{padding:5px 8px 4px}
.head-grey{background:var(--grey-dark)}
.head-orange{background:var(--orange)}
.call-bar{background:var(--navy);color:#fff;font-family:"Montserrat",sans-serif;font-weight:700;font-size:8.4px;text-align:center;padding:6px 0}

.triage-table{position:absolute;left:28px;top:238px;width:706px;border-collapse:collapse;table-layout:fixed;font-size:7px;line-height:1.38}
.triage-table th{background:var(--blue);color:#fff;font-family:"Montserrat",sans-serif;font-weight:700;font-size:8.2px;height:17px;border-right:1px solid #fff}
.triage-table th.col-instruction{background:var(--navy-deep)}
.triage-table th.cat-6{background:var(--blue-light)}
.triage-table td{vertical-align:top;border:1px solid #d5d9df;padding:4px 4px}
.row-symptoms td{height:136px}
.row-symptoms td:first-child{color:var(--muted)}
.row-tell td{background:var(--navy);color:#fff;font-family:"Montserrat",sans-serif;font-weight:700;font-size:6.6px;text-align:center;vertical-align:middle;height:36px;border-color:var(--navy)}
.row-tell td:first-child{text-align:left;font-family:"Open Sans",sans-serif;font-weight:400;font-size:7px}
.row-action td{color:var(--orange);font-weight:700;text-align:center;vertical-align:middle;height:29px}
.row-admin td{color:var(--muted);text-align:center;vertical-align:middle;height:30px}
.row-action td:first-child,.row-admin td:first-child{color:var(--ink);font-weight:400;text-align:left}
.front-rule{left:0;top:492px;width:765px;height:1.5px;background:var(--navy)}
.front-foot{left:0;top:510px;width:765px;text-align:center;font-size:7px;color:var(--muted)}

/* ---------- BACK ---------- */
.back-band{left:0;top:0;width:765px;height:42px;background:linear-gradient(90deg,var(--navy-deep),var(--blue));display:flex;align-items:center;padding-left:26px;color:#fff;font-family:"Montserrat",sans-serif;font-weight:800;font-size:13.4px;white-space:nowrap;border-bottom:2px solid var(--blue-light)}
.back-band .dot{display:inline-block;width:8px;height:8px;border-radius:50%;background:var(--orange);margin:0 12px}
.col{position:absolute;font-size:7.6px;line-height:1.34}
.col-left{left:26px;top:56px;width:220px}
.col-mid{left:260px;top:42px;width:238px;height:454px;background:var(--panel);padding:14px 12px 0 12px}
.col-right{left:510px;top:184px;width:218px}
.sec-title{font-family:"Montserrat",sans-serif;font-weight:800;font-size:9.6px;color:var(--orange);margin-bottom:6px}
.sec-title.blue{color:var(--blue)}
.sec-title + .ticks,.sec-title + .steps{margin-bottom:9px}
.col .ticks li{margin-bottom:5px;text-align:justify}
.steps{list-style:none}
.steps li{margin-bottom:5px}
.steps li b{font-weight:400;margin-right:6px}
.hl{color:var(--orange);font-weight:600}
.note-orange{color:var(--orange);margin-top:6px}

.plan-box{position:absolute;left:26px;top:374px;width:218px;border:1px dashed #b9bec6;font-size:7.6px;line-height:1.5}
.plan-box .ticks{padding:4px 7px 4px}

.photo{position:absolute;left:498px;top:42px;width:267px;height:142px;background:linear-gradient(180deg,#c9dcef 0%,#e4eef8 60%,#fff 100%)}
.back-brand{left:640px;top:436px;width:100px;text-align:center;color:var(--navy);font-weight:700;font-size:8.4px;line-height:1.25;letter-spacing:.4px}
.back-brand .brand-mark{width:14px;height:14px;margin-bottom:5px}
.back-rule{left:0;top:496px;width:700px;height:1.5px;background:var(--navy)}
.back-foot{left:26px;top:507px;font-size:7px;font-style:italic;color:var(--ink)}
</style>
</head>
<body>

<section class="page sheet-front">
  <svg class="abs front-header" width="765" height="106" viewBox="0 0 765 106" aria-hidden="true">
    <polygon points="186,0 765,0 765,106 224,106" fill="#f78f20"/>
    <polygon points="198,0 765,0 765,96 232,96" fill="#0b3d8c"/>
  </svg>
  <div class="abs brand"><span class="brand-mark"></span>HARLOW ACADEMY<br>OF LEARNING</div>
  <h1 class="abs doc-title">TRIAGE: A GUIDE TO URGENCY FOR NON-CLINICAL<br>STAFF IN GENERAL PRACTICE FOR TELEPHONE<br>AND WALK IN PRESENTATIONS</h1>
  <div class="abs tool-badge">
    <svg width="22" height="22" viewBox="0 0 24 24" aria-hidden="true"><circle cx="12" cy="12" r="7" fill="none" stroke="#fff" stroke-width="3"/><g stroke="#fff" stroke-width="3"><line x1="12" y1="1" x2="12" y2="5"/><line x1="12" y1="19" x2="12" y2="23"/><line x1="1" y1="12" x2="5" y2="12"/><line x1="19" y1="12" x2="23" y2="12"/><line x1="4" y1="4" x2="7" y2="7"/><line x1="17" y1="17" x2="20" y2="20"/><line x1="4" y1="20" x2="7" y2="17"/><line x1="17" y1="7" x2="20" y2="4"/></g></svg>
    TOOL
  </div>

  <div class="pill pill-orange" style="left:28px;top:132px;width:174px;height:22px">Do you have an urgent problem?</div>
  <div class="pill pill-grey" style="left:212px;top:132px;width:62px;height:22px">YES</div>
  <div class="pill pill-navy" style="left:62px;top:162px;width:106px;height:22px">No / I Don't Know</div>
  <div class="pill pill-orange pill-two" style="left:28px;top:192px;width:174px;height:29px">The next available appointment is ....<br>Is this ok?</div>
  <div class="pill pill-grey" style="left:212px;top:192px;width:62px;height:29px">NO</div>

  <div class="infobox" style="left:288px;top:120px;width:218px">
    <div class="infobox-head head-grey">Record the patient's phone number</div>
    <ul class="ticks">
      <li>What is the name and age of the patient?</li>
      <li>What is the nature of the problem?</li>
      <li>What is the duration of the problem?</li>
      <li>What is the severity of the problem?</li>
      <li>Has the patient had any previous major health problems?</li>
      <li>Select a category below and follow instructions.</li>
    </ul>
  </div>

  <div class="infobox" style="left:516px;top:120px;width:218px">
    <div class="infobox-head head-orange">EMERGENCY ACTION PLAN</div>
    <ul class="ticks navy">
      <li>Remain calm and do not panic.</li>
      <li>Be aware and respond to the needs of the emergency.</li>
      <li>Assess which patient needs to take priority.</li>
      <li>Deal with any injury or illness in order of severity.</li>
    </ul>
    <div class="call-bar">CALL 000 FOR AMBULANCE, POLICE OR FIRE</div>
  </div>

  <table class="triage-table">
    <colgroup><col style="width:62px"><col><col><col><col><col><col></colgroup>
    <tr>
      <th class="col-instruction">Instruction</th><th>Category 1</th><th>Category 2</th><th>Category 3</th><th>Category 4</th><th>Category 5</th><th class="cat-6">Category 6</th>
    </tr>
    <tr class="row-symptoms">
      <td>Practice to ask the patient or caller to describe the problem/s,and categorise accordingly:</td>
      <td><ul class="ticks"><li>Chest pain</li><li>Breathing difficulties/ trouble talking</li><li>Facial swelling and rash</li><li>Collapse/altered consciousness</li><li>Facial/limb weakness</li><li>Extensive burns</li><li>Sick patient you have concerns about</li></ul></td>
      <td><ul class="ticks"><li>Fitting</li><li>Bleeding (heavy or persistent)</li><li>Spinal or head injury/ trauma</li><li>Snake bite</li><li>Heart palpitations</li><li>In labour/ruptured membranes</li><li>Neck stiffness/altered consciousness</li></ul></td>
      <td><ul class="ticks"><li>Unable to urinate</li><li>Unwell 'floppy' infant</li><li>Poisoning/overdose</li><li>Eye injuries/chemical in the eye</li><li>Pain (severe)</li><li>Injured limb/possible fracture</li></ul></td>
      <td><ul class="ticks"><li>Unwell child/elder with fever, vomiting, diarrhoea or pain for &gt;24 hours</li><li>Pregnancy: pain or bleeding; reduced foetal movement</li><li>Abuse or assault</li><li>Visual disturbance</li><li>Patient or carer with extreme concern</li><li>Psychological distress</li></ul></td>
      <td><ul class="ticks"><li>Unwell child/elderly with fever, vomiting, diarrhoea or pain for &lt;24 hours</li><li>Rash (severe)</li><li>Cut/laceration</li><li>Severe flu like symptoms</li></ul></td>
      <td><ul class="ticks"><li>Adult with fever, but otherwise well</li><li>Post op problems</li><li>Eye or ear infections/pain</li><li>Adult with continuous vomiting and/or diarrhoea for &gt;24 hrs</li></ul></td>
    </tr>
    <tr class="row-tell">
      <td>Tell the caller to:</td>
      <td>Call 000</td>
      <td>Go to emergency department now</td>
      <td>Put call through to nurse/doctor</td>
      <td>Come to surgery now Advise the on-call nurse/doctor</td>
      <td>Come to surgery today and call back if gets worse</td>
      <td>Make an appointment within 24 hours and call back if gets worse</td>
    </tr>
    <tr class="row-action">
      <td>Practice/ Receptionist</td>
      <td>Call nurse/doctor<br>for help immediately</td>
      <td>Interrupt nurse/doctor immediately</td>
      <td>Advise nurse/<br>doctor now</td>
      <td>Discuss with nurse/doctor</td>
      <td>Inform nurse/doctor within 30 minutes</td>
      <td>Inform nurse/doctor</td>
    </tr>
    <tr class="row-admin">
      <td>Practice/ Receptionist</td>
      <td>Retrieve patient file<br>Document activity</td>
      <td>Retrieve patient file<br>Document activity</td>
      <td>Retrieve patient file<br>Document activity</td>
      <td>Retrieve patient file<br>Document activity</td>
      <td>Retrieve patient file<br>Document activity</td>
      <td>Retrieve patient file<br>Document activity</td>
    </tr>
  </table>

  <div class="abs front-rule"></div>
  <p class="abs front-foot">Lorem Ipsum is simply dummy text of the printing and typesetting industry. Lorem Ipsum has been the industry's standard dummy text ever since the 1500s,</p>
</section>

<section class="page sheet-back">
  <div class="abs back-band">FRONT DESK TRIAGE<span class="dot"></span>HOW TO MANAGE COMMON SCENARIOS FACED BY RECEPTION STAFF</div>

  <div class="col col-left">
    <h2 class="sec-title">IS THIS AN EMERGENCY?</h2>
    <ul class="ticks">
      <li>When answering the telephone, all callers should be asked if the matter is an emergency prior to being placed on hold: Ask the patient, "Is this an emergency or can I place you on hold for a moment?"</li>
      <li>Consider the TRIAGE STEPS and CATEGORIES listed on the reverse of this document to assess the patient's status.</li>
    </ul>
    <h2 class="sec-title">ASK THE PATIENT – TRIAGE STEPS</h2>
    <ol class="steps">
      <li><b>1.</b> Confirm the patient's name and phone number.</li>
      <li><b>2.</b> Does the patient attend the surgery? (ie Does the practice have previous medical records to hand?)</li>
      <li><b>3.</b> Location. ("Are you at home?" "Are you alone?")</li>
      <li><b>4.</b> Nature of their problem. (Patient may prefer to speak to the practice nurse or on call doctor.)</li>
      <li><b>5.</b> Duration of their symptoms. ("How long have you felt like this?")</li>
      <li><b>6.</b> Severity of their problem. ("On a scale of 1 to 10 how severe is the pain?" [if applicable].)</li>
      <li><b>7.</b> Any previous major health problems. ("Are you on any medication?" "Do you have any allergies?")</li>
    </ol>
  </div>

  <div class="plan-box">
    <div class="infobox-head head-orange">EMERGENCY ACTION PLAN</div>
    <ul class="ticks navy">
      <li>Remain calm and do not panic.</li>
      <li>Be aware and respond to the needs of the emergency.</li>
      <li>Assess which patient needs to take priority.</li>
      <li>Deal with any injury or illness in order of severity.</li>
    </ul>
    <div class="call-bar">CALL 000 FOR AMBULANCE, POLICE OR FIRE</div>
  </div>

  <div class="col col-mid">
    <h2 class="sec-title blue">ON THE DAY EMERGENCIES IN THE CLINIC</h2>
    <ul class="ticks">
      <li><span class="hl">Category 1</span> patients should immediately be seen by the on-call doctor or other medical professional on duty.</li>
      <li><span class="hl">Category 2</span> patients should be directed to the emergency department of their nearest hospital.</li>
      <li><span class="hl">Category 3</span> patients or patients with worsening symptoms should be referred to the practice nurse or on call doctor.</li>
      <li><span class="hl">Category 4</span> patients should be advised to attend the clinic immediately and triaged by the practice nurse (may then be slotted in between appointments or at the end of the session).</li>
      <li><span class="hl">Category 5</span> patients should make an appointment for the day and be advised to call back if symptoms worsen.</li>
      <li><span class="hl">Category 6</span> patients should make an appointment within 24 hours and call back if symptoms worsen.</li>
    </ul>
    <h2 class="sec-title blue">PATIENTS PRESENTING WITH SYMPTOMS OF POTENTIAL COMMUNICABLE DISEASES</h2>
    <ul class="ticks">
      <li>Such as 'influenza'(flu), measles, chicken pox should be isolated to a secluded area of the medical practice such as the nurses' office. Where possible, a notice of isolation is to be fixed to the door to limit access in this area.</li>
      <li>Patients with 'flu like symptoms should be required to wear a surgical mask.</li>
      <li>If the patient is bleeding or vomiting, put gloves on before you assist them.</li>
    </ul>
    <h2 class="sec-title">SCHEDULING CARE</h2>
    <ul class="ticks">
      <li>Reception staff should reserve several unbooked appointment times each day for 'on the day' urgent appointments such as unwell children and the elderly, lacerations and suspected fractures.</li>
    </ul>
  </div>

  <div class="photo" role="img" aria-label="Photo of a smiling female doctor with a stethoscope and colleagues in a bright clinic"></div>

  <div class="col col-right">
    <ul class="ticks">
      <li>If your practice does not operate on an appointment system, patients should be triaged on walk in and advised of the expected waiting time to see the doctor, nurse or Aboriginal health worker.</li>
      <li>Where a patient is assessed as in need of urgent medical attention over the telephone, advise the caller to hang up and call 000 immediately for an ambulance.</li>
      <li>Where a receptionist is unable to determine the urgency of a telephone call, the patient should be transferred to the practice nurse or on-call doctor for triage.</li>
      <li>If a patient presents in person and requires urgent medical assistance after the doctor has left – call 000 for ambulance.</li>
      <li>Clinical staff treating the patient should wear as a minimum, a surgical mask, gloves and when collecting nose and/or throat swabs, protective eyewear.</li>
    </ul>
    <p class="note-orange">All emergency cases dealt with by reception should be recorded by the staff member involved in the patient health record in addition to the clinical notes recorded by the practice nurse or doctor/s treating the patient.</p>
  </div>

  <div class="abs back-brand"><span class="brand-mark"></span>HARLOW ACADEMY<br>OF LEARNING</div>

  <div class="abs back-rule"></div>
  <p class="abs back-foot">This resource was developed by Clinic Circle Eastgate (2010) and recreated with permission from Southern Basin Careline Hub (2014)</p>
</section>

</body>
</html>
```